Quimby's Yard & Garden Center Business Card Update

I need an updated Business card design for my Lawn and Garden Center. We do Landscaping installs, Lawn Mowing, Snow Removal and also have a Garden Center Retail Division. I uploaded a few of our previous business cards to give an idea of what we are starting with. The main goal of this update is to simplify and modernize the business card, not all of the services that are on the previous cards has to be on the new one but I would still like to highlight our main services. There is also a sample of our logo that Can be used in the design.

Industry/Entity Type

Landscaping

Contact Information for Business Card

Morris Quimby
Morris@Quimbysyardandgarden.example
Business (555) 201-7784
Cell (555) 318-6092

Colors

Designer to choose colors to be used in the design.

Requirements
Must have
• Services Provided :
• Landscaping
• Lawn Maintenance
• Snow Removal
• Garden Center

```html
<!DOCTYPE html>
<html lang="en">
<head>
<meta charset="utf-8">
<title>Quimby's Yard &amp; Garden Center – Business Cards</title>
<link rel="stylesheet" href="https://fonts.googleapis.com/css2?family=Crimson+Text:wght@400;600&family=Open+Sans:wght@400;700&family=Roboto+Condensed:wght@400;700&display=swap">
<style>
  :root {
    --page: #ecebe7;
    --green-deep: #003d0c;
    --green-mid: #0d6b1c;
    --green-glow: #1f8a2a;
    --green-pill: #1f5512;
    --mint: #c9f5c2;
    --mint-soft: #e3fbe0;
    --leaf: #a8e890;
    --white: #ffffff;
    --ink-dark: #1d4a14;
    --clover-a: #27511f;
    --clover-b: #13320f;
  }
  * { box-sizing: border-box; margin: 0; padding: 0; }
  html, body { width: 1200px; height: 900px; overflow: hidden; }
  body {
    background: var(--page);
    position: relative;
    font-family: "Open Sans", sans-serif;
  }
  .card {
    position: absolute;
    left: 280px;
    width: 640px;
    height: 366px;
    overflow: hidden;
    box-shadow: 0 6px 18px rgba(0,0,0,.18);
  }

  /* ---------- Front card ---------- */
  .card--front {
    top: 66px;
    background: radial-gradient(ellipse at 42% 40%, var(--green-glow) 0%, var(--green-mid) 30%, var(--green-deep) 75%);
    color: var(--white);
  }
  .front-decor { position: absolute; inset: 0; }
  .front-divider {
    position: absolute; left: 40px; right: 250px; top: 188px;
    height: 1px; background: rgba(120, 220, 120, .45);
  }
  .front-contact { position: absolute; left: 40px; top: 54px; }
  .front-contact .person { font-weight: 700; font-size: 18px; color: var(--mint); margin-bottom: 6px; }
  .contact-line {
    display: flex; align-items: center; gap: 8px;
    font-weight: 700; font-size: 15px; line-height: 1.5; color: var(--mint);
    white-space: nowrap;
  }
  .contact-icon { width: 15px; height: 15px; flex: none; }
  .floral { position: absolute; left: 40px; top: 214px; }
  .floral .floral-title { font-weight: 700; font-size: 17px; color: var(--mint); margin-bottom: 4px; }
  .floral .floral-items { font-size: 15px; line-height: 1.4; color: var(--mint); }
  .front-brand {
    position: absolute; right: 20px; top: 58px; width: 220px; text-align: center;
  }
  .brand-mark {
    display: inline-flex; align-items: center; gap: 10px;
    font-family: "Roboto Condensed", sans-serif; font-weight: 700;
    font-size: 42px; color: var(--leaf); white-space: nowrap;
  }
  .brand-dot { width: 16px; height: 16px; background: var(--leaf); border-radius: 50%; }
  .front-brand .company {
    font-family: "Crimson Text", serif; font-size: 16px; margin-top: 10px; color: var(--white);
    white-space: nowrap;
  }
  .front-brand .llc { font-family: "Crimson Text", serif; font-size: 16px; color: var(--white); }

  /* ---------- Back card ---------- */
  .card--back { top: 474px; background: var(--white); }
  .back-art { position: absolute; inset: 0; }
  .back-brand {
    position: absolute; left: 24px; top: 70px; width: 270px; text-align: center; color: var(--white);
  }
  .back-brand .brand-mark { font-size: 36px; }
  .back-brand .title {
    font-family: "Crimson Text", serif; font-weight: 600; font-size: 33px; line-height: 1.08; margin-top: 12px;
    white-space: nowrap;
  }
  .back-brand .llc { font-family: "Crimson Text", serif; font-size: 19px; margin-top: 2px; }
  .back-url {
    position: absolute; left: 24px; bottom: 20px;
    font-family: "Roboto Condensed", sans-serif; font-size: 14px; color: var(--white);
    white-space: nowrap;
  }
  .back-contact { position: absolute; right: 30px; top: 22px; width: 210px; color: var(--ink-dark); }
  .back-contact .person { font-weight: 700; font-size: 14px; white-space: nowrap; }
  .back-contact .contact-line { color: var(--ink-dark); font-size: 14px; line-height: 1.4; }
  .back-contact .contact-icon { width: 12px; height: 12px; }
  .services { position: absolute; right: 30px; top: 100px; width: 210px; font-family: "Roboto Condensed", sans-serif; }
  .services-pill {
    display: inline-block; background: var(--green-pill); color: var(--white);
    font-weight: 700; font-size: 18px; padding: 5px 16px; border-radius: 18px; margin-bottom: 8px;
    white-space: nowrap;
  }
  .services-list { list-style: none; color: var(--ink-dark); font-size: 16px; line-height: 1.25; padding-left: 12px; }
  .services-list li::before { content: "•"; margin-right: 2px; }
  .address-pill {
    position: absolute; right: 16px; bottom: 24px;
    display: flex; align-items: center; gap: 8px;
    background: var(--green-pill); color: var(--white);
    font-family: "Roboto Condensed", sans-serif; font-weight: 700; font-size: 15px;
    padding: 6px 16px 6px 8px; border-radius: 20px; white-space: nowrap;
  }
  .address-pill .contact-icon { width: 18px; height: 18px; }
</style>
</head>
<body>

<section class="card card--front">
  <svg class="front-decor" width="640" height="366" viewBox="0 0 640 366" aria-hidden="true">
    <polygon points="420,150 460,140 485,165 470,200 430,200 413,178" fill="#5fbf6a" opacity=".3"/>
    <polygon points="445,185 490,175 515,205 495,245 450,240 435,212" fill="#5fbf6a" opacity=".24"/>
  </svg>
  <div class="front-divider"></div>

  <div class="front-contact">
    <p class="person">Morris &amp; Greta Quimby</p>
    <p class="contact-line">
      <svg class="contact-icon" viewBox="0 0 16 16"><circle cx="8" cy="8" r="8" fill="#c9f5c2"/><path d="M5 4l2 2-1 1c.5 1 1.5 2 3 3l1-1 2 2-1 1.5C8 12 4 8 3.8 5z" fill="#003d0c"/></svg>
      (555) 201-7784
    </p>
    <p class="contact-line">
      <svg class="contact-icon" viewBox="0 0 16 16"><rect x="1" y="3" width="14" height="10" rx="2" fill="#c9f5c2"/><rect x="4" y="5" width="8" height="3" fill="#003d0c"/></svg>
      (555) 402-1186
    </p>
    <p class="contact-line">
      <svg class="contact-icon" viewBox="0 0 16 16"><circle cx="8" cy="8" r="8" fill="#c9f5c2"/><rect x="4" y="5" width="8" height="6" fill="#003d0c"/><path d="M4 5l4 3 4-3" stroke="#c9f5c2" fill="none"/></svg>
      greta@quimbysyardandgarden.example
    </p>
  </div>

  <div class="floral">
    <p class="floral-title">Full Service Fresh Floral Department</p>
    <p class="floral-items">• Wedding &nbsp;• Funeral &nbsp;• Special Occasions<br>• Delivery Service Available</p>
  </div>

  <div class="front-brand">
    <p class="brand-mark"><span class="brand-dot"></span>Quimby's</p>
    <p class="company">Quimby's Yard &amp; Garden Center</p>
    <p class="llc">(LLC)</p>
  </div>
</section>

<section class="card card--back">
  <svg class="back-art" width="640" height="366" viewBox="0 0 640 366">
    <defs>
      <linearGradient id="cloverFill" x1="0" y1="0" x2="1" y2="1">
        <stop offset="0" stop-color="var(--clover-a)"/>
        <stop offset="1" stop-color="var(--clover-b)"/>
      </linearGradient>
    </defs>
    <polygon points="470,0 640,0 640,140" fill="#e3fbe0"/>
    <polygon points="540,140 610,120 640,200 590,260" fill="#d4f7cd" opacity=".8"/>
    <polygon points="0,0 300,0 400,366 0,366" fill="url(#cloverFill)" role="img" aria-label="Photograph of a dense bed of green clover leaves"/>
  </svg>

  <div class="back-brand">
    <p class="brand-mark"><span class="brand-dot"></span>Quimby's</p>
    <p class="title">Quimby's Yard<br>&amp;<br>Garden Center</p>
    <p class="llc">(LLC)</p>
  </div>
  <p class="back-url">https://quimbysyardandgarden.example/</p>

  <div class="back-contact">
    <p class="person">Morris &amp; Greta Quimby</p>
    <p class="contact-line">
      <svg class="contact-icon" viewBox="0 0 16 16"><circle cx="8" cy="8" r="8" fill="#1d4a14"/><path d="M5 4l2 2-1 1c.5 1 1.5 2 3 3l1-1 2 2-1 1.5C8 12 4 8 3.8 5z" fill="#fff"/></svg>
      (555) 201-7784
    </p>
    <p class="contact-line">
      <svg class="contact-icon" viewBox="0 0 16 16"><rect x="1" y="3" width="14" height="10" rx="2" fill="#1d4a14"/><rect x="4" y="5" width="8" height="3" fill="#fff"/></svg>
      (555) 402-1186
    </p>
  </div>

  <div class="services">
    <p class="services-pill">Services Provided :</p>
    <ul class="services-list">
      <li>Landscaping</li>
      <li>Lawn Maintenance</li>
      <li>Snow Removal</li>
      <li>Garden Center</li>
      <li>Tree Transplanting</li>
    </ul>
  </div>

  <p class="address-pill">
    <svg class="contact-icon" viewBox="0 0 18 18"><circle cx="9" cy="9" r="9" fill="#fff"/><path d="M9 3.5a3.5 3.5 0 0 0-3.5 3.5c0 2.8 3.5 7 3.5 7s3.5-4.2 3.5-7A3.5 3.5 0 0 0 9 3.5z" fill="#1f5512"/><circle cx="9" cy="7" r="1.3" fill="#fff"/></svg>
    48, Elm Row Ada, OH-40000
  </p>
</section>

</body>
</html>
```